Quillmoor Tesk Centre needs signs

We are looking to create three signs for our business. We need a 605 x 60 cm sign above the front door of the business and a smaller sign that is 153 x 90 cm. I have attached some basic ideas we have come up with but need something a lot more catchy.

```html
<!DOCTYPE html>
<html lang="en">
<head>
<meta charset="utf-8">
<title>Quillmoor Tesk Centre – Signage</title>
<link rel="stylesheet" href="https://fonts.googleapis.com/css2?family=Bebas+Neue&family=Lato:wght@400;700&display=swap">
<style>
  :root {
    --purple: #6b2c8d;
    --white: #ffffff;
    --ink: #1a1a1a;
    --green-light: #b5d334;
    --green-deep: #7cc142;
    --page: #ffffff;
  }
  html, body {
    margin: 0;
    padding: 0;
    width: 1200px;
    height: 878px;
    overflow: hidden;
    background: var(--page);
  }
  .sheet {
    position: relative;
    width: 1200px;
    height: 878px;
    font-family: "Lato", sans-serif;
  }
  .size-label {
    position: absolute;
    left: 22px;
    margin: 0;
    font-family: "Lato", sans-serif;
    font-weight: 400;
    font-size: 23px;
    color: var(--ink);
    line-height: 1;
  }
  .size-label--wide { top: 19px; }
  .size-label--panel { top: 479px; }
  .sign {
    position: absolute;
    display: block;
  }
  .sign__ground { fill: var(--purple); }
  .sign__mark { fill: var(--white); }
  .sign__name {
    font-family: "Bebas Neue", sans-serif;
    fill: var(--white);
  }
  .sign__tagline {
    font-family: "Lato", sans-serif;
    font-weight: 700;
    fill: var(--white);
  }
  .sign__tagline--dark { fill: var(--ink); }
  .sign__bullet { fill: var(--white); }
  .sign__bullet--dark { fill: var(--ink); }
  .sign__swoosh { fill: url(#band-green); }
  .sign__stripe { fill: var(--green-deep); }
</style>
</head>
<body>
<main class="sheet">

  <p class="size-label size-label--wide">Signage 605 x 60cm</p>

  <!-- Fascia option 1: name only -->
  <svg class="sign sign--fascia" style="left:22px;top:59px" width="1158" height="114" viewBox="0 0 1158 114">
    <rect class="sign__ground" width="1158" height="114"/>
    <circle class="sign__mark" cx="145" cy="57" r="18"/>
    <text class="sign__name" x="191" y="96" font-size="104" textLength="777" lengthAdjust="spacingAndGlyphs">QUILLMOOR TESK CENTRE</text>
  </svg>

  <!-- Fascia option 2: name with services line -->
  <svg class="sign sign--fascia" style="left:22px;top:190px" width="1158" height="114" viewBox="0 0 1158 114">
    <rect class="sign__ground" width="1158" height="114"/>
    <circle class="sign__mark" cx="145" cy="55" r="16"/>
    <text class="sign__name" x="191" y="63" font-size="64" textLength="777" lengthAdjust="spacingAndGlyphs">QUILLMOOR TESK CENTRE</text>
    <text class="sign__tagline" x="191" y="95" font-size="25" textLength="316" lengthAdjust="spacingAndGlyphs">Massage &amp; Reiki Therapy</text>
    <ellipse class="sign__bullet" cx="525" cy="87" rx="7" ry="9" transform="rotate(20 525 87)"/>
    <text class="sign__tagline" x="544" y="95" font-size="25" textLength="431" lengthAdjust="spacingAndGlyphs">Weight Loss &amp; Wellness Programs</text>
  </svg>

  <!-- Fascia option 3: name with green band -->
  <svg class="sign sign--fascia" style="left:22px;top:320px" width="1158" height="116" viewBox="0 0 1158 116">
    <defs>
      <linearGradient id="band-green" x1="0" y1="0" x2="1" y2="0">
        <stop offset="0" stop-color="#a8cf38"/>
        <stop offset="1" stop-color="#7cc142"/>
      </linearGradient>
      <linearGradient id="band-fade" x1="0" y1="0" x2="0" y2="1">
        <stop offset="0.7" stop-color="#ffffff" stop-opacity="0"/>
        <stop offset="1" stop-color="#ffffff" stop-opacity="0.75"/>
      </linearGradient>
    </defs>
    <rect class="sign__ground" width="1158" height="116"/>
    <path class="sign__swoosh" d="M0,70 C260,82 560,78 820,66 C960,60 1080,50 1158,42 L1158,116 L0,116 Z"/>
    <rect width="1158" height="116" fill="url(#band-fade)"/>
    <circle class="sign__mark" cx="145" cy="45" r="16"/>
    <text class="sign__name" x="191" y="64" font-size="66" textLength="777" lengthAdjust="spacingAndGlyphs">QUILLMOOR TESK CENTRE</text>
    <text class="sign__tagline sign__tagline--dark" x="189" y="102" font-size="20.5" textLength="309" lengthAdjust="spacingAndGlyphs">MASSAGE &amp; REIKI THERAPY</text>
    <ellipse class="sign__bullet sign__bullet--dark" cx="517" cy="95" rx="6" ry="8" transform="rotate(20 517 95)"/>
    <text class="sign__tagline sign__tagline--dark" x="534" y="102" font-size="20.5" textLength="445" lengthAdjust="spacingAndGlyphs">WEIGHT LOSS &amp; WELLNESS PROGRAMS</text>
  </svg>

  <p class="size-label size-label--panel">Signage 153 x 90cm</p>

  <!-- Panel option 1 -->
  <svg class="sign sign--panel" style="left:22px;top:520px" width="565" height="334" viewBox="0 0 565 334">
    <rect class="sign__ground" width="565" height="334"/>
    <circle class="sign__mark" cx="80" cy="167" r="34"/>
    <text class="sign__name" x="360" y="106" font-size="110" text-anchor="middle" textLength="318" lengthAdjust="spacingAndGlyphs">QUILLMOOR</text>
    <text class="sign__name" x="360" y="206" font-size="110" text-anchor="middle">TESK</text>
    <text class="sign__name" x="360" y="308" font-size="110" text-anchor="middle" textLength="218" lengthAdjust="spacingAndGlyphs">CENTRE</text>
  </svg>

  <!-- Panel option 2: with green stripe -->
  <svg class="sign sign--panel" style="left:613px;top:520px" width="567" height="334" viewBox="0 0 567 334">
    <rect class="sign__ground" width="567" height="334"/>
    <path class="sign__stripe" d="M168,0 C190,55 186,115 154,172 C136,215 146,285 182,334 L172,334 C136,285 126,215 145,172 C176,115 180,55 160,0 Z"/>
    <circle class="sign__mark" cx="85" cy="167" r="34"/>
    <text class="sign__name" x="362" y="106" font-size="110" text-anchor="middle" textLength="318" lengthAdjust="spacingAndGlyphs">QUILLMOOR</text>
    <text class="sign__name" x="362" y="206" font-size="110" text-anchor="middle">TESK</text>
    <text class="sign__name" x="362" y="308" font-size="110" text-anchor="middle" textLength="218" lengthAdjust="spacingAndGlyphs">CENTRE</text>
  </svg>

</main>
</body>
</html>
```